Shine Barn Auto Care Business Card

2 side business card design for an auto detailing business

Target Market(s)

Auto detailing

Contact Information for Business Card

Things included

The business name “Shine Barn Auto Care”
Owen Marchetti
(403)871-2964
Carrow Bend, Sk

Services offered - complete interior& exterior detail
- paint correction & protection
- ceramic coating
- trim restore
- auto carpet & seat cleaning

Requirements
Must have
• Colours that are in my logo

Services offered

My name Owen Marchetti
403-871-2964
Carrow Bend, Sk

Not too sure in what order for these ?
Website. Shinebarnautocare.com
Instagram Shinebarnautocare
Email. Shinebarnautoac@mailbox-example.com

```html
<!DOCTYPE html>
<html lang="en">
<head>
<meta charset="utf-8">
<title>Shine Barn Auto Care – Business Card</title>
<link href="https://fonts.googleapis.com/css2?family=Arimo:wght@400;700&family=Michroma&display=swap" rel="stylesheet">
<style>
  :root {
    --page: #b9b9b9;
    --red: #990000;
    --red-deep: #8a0000;
    --red-light: #a80d0d;
    --white: #ffffff;
    --ink: #111111;
    --rule-light: rgba(255,255,255,0.75);
    --rule-dark: #9a9a9a;
  }
  * { margin: 0; padding: 0; box-sizing: border-box; }
  html, body {
    width: 1200px; height: 1200px; overflow: hidden;
    background: var(--page);
    font-family: "Arimo", Arial, sans-serif;
  }
  .canvas { position: relative; width: 1200px; height: 1200px; }

  .card {
    position: absolute; top: 303px; width: 370px; height: 594px;
    border-radius: 12px; text-align: center;
    box-shadow: 3px 4px 6px rgba(0,0,0,0.35);
  }
  .card--front {
    left: 200px;
    background: radial-gradient(ellipse at 50% 40%, var(--red-light) 0%, var(--red) 55%, var(--red-deep) 100%);
    color: var(--white);
  }
  .card--back { left: 600px; top: 305px; width: 362px; height: 591px; background: var(--white); color: var(--ink); }

  .block { position: absolute; left: 0; width: 100%; }

  .brand-ring {
    position: absolute; left: 50%; top: 78px; width: 104px; height: 104px;
    margin-left: -52px; border-radius: 50%; border: 7px solid currentColor;
  }
  .card--back .brand-ring { top: 76px; color: var(--red); }

  .brand-name {
    top: 198px; font-weight: 700; font-size: 30px; line-height: 32px;
    letter-spacing: 1px; text-transform: uppercase;
  }
  .card--back .brand-name { top: 196px; color: var(--ink); }

  .services-heading {
    top: 330px; font-weight: 700; font-size: 18px;
    display: flex; align-items: center; justify-content: center; gap: 8px;
  }
  .services-heading::before, .services-heading::after {
    content: ""; width: 48px; height: 1px; background: var(--white);
  }
  .services-sub { top: 354px; font-size: 13.5px; text-transform: uppercase; }
  .services-list { top: 386px; font-size: 19px; line-height: 26.8px; list-style: none; }

  .divider {
    position: absolute; left: 50%; transform: translateX(-50%);
    display: flex; align-items: center; gap: 4px;
  }
  .divider .rule { height: 1px; }
  .card--front .divider .rule { background: var(--rule-light); }
  .card--back .divider .rule { background: var(--rule-dark); }

  .social-dot { width: 22px; height: 22px; border-radius: 50%; background: var(--white); }
  .handle { top: 540px; font-size: 17px; }

  .person-name {
    top: 348px; font-family: "Michroma", sans-serif; font-size: 20px;
    color: var(--red); letter-spacing: 1px; text-transform: uppercase;
  }
  .contact-icon { width: 25px; height: 25px; display: block; }
  .contact-lines { top: 425px; font-size: 16.5px; line-height: 21.5px; }
  .contact-lines .accent { color: var(--red); }
  .city { top: 529px; font-size: 17px; }
</style>
</head>
<body>
<div class="canvas">

  <section class="card card--front">
    <div class="brand-ring"></div>
    <div class="block brand-name">Shine Barn<br>Auto Care</div>

    <h2 class="block services-heading">SERVICES OFFERED</h2>
    <p class="block services-sub">Complete interior &amp; exterior detail</p>
    <ul class="block services-list">
      <li>Paint correction &amp; protection</li>
      <li>Ceramic coating</li>
      <li>Trim restore</li>
      <li>Auto carpet &amp; seat cleaning</li>
    </ul>

    <div class="divider" style="top:513px">
      <span class="rule" style="width:136px"></span>
      <span class="social-dot"></span>
      <span class="rule" style="width:130px"></span>
    </div>
    <p class="block handle">Shinebarnautocare</p>
  </section>

  <section class="card card--back">
    <div class="brand-ring"></div>
    <div class="block brand-name">Shine Barn<br>Auto Care</div>

    <h1 class="block person-name">Owen Marchetti</h1>

    <div class="divider" style="top:391px">
      <span class="rule" style="width:50px"></span>
      <svg class="contact-icon" viewBox="0 0 26 26" aria-label="Phone">
        <circle cx="13" cy="13" r="11.5" fill="none" stroke="#990000" stroke-width="1.5"/>
        <path d="M9 7.5l2 0 1 3-1.4 1.2a7 7 0 0 0 3.7 3.7L15.5 14l3 1v2a1.5 1.5 0 0 1-1.6 1.5A10 10 0 0 1 7.5 9.1 1.5 1.5 0 0 1 9 7.5z" fill="#990000"/>
      </svg>
      <svg class="contact-icon" viewBox="0 0 26 26" aria-label="Email">
        <circle cx="13" cy="13" r="11.5" fill="none" stroke="#990000" stroke-width="1.5"/>
        <rect x="7" y="8.5" width="12" height="9" fill="#990000"/>
        <path d="M7 8.5l6 5 6-5" fill="none" stroke="#fff" stroke-width="1"/>
      </svg>
      <svg class="contact-icon" viewBox="0 0 26 26" aria-label="Website">
        <circle cx="13" cy="13" r="11.5" fill="none" stroke="#990000" stroke-width="1.5"/>
        <circle cx="13" cy="13" r="6.5" fill="#990000"/>
        <path d="M6.5 13h13M13 6.5c-2.5 3-2.5 10 0 13M13 6.5c2.5 3 2.5 10 0 13" fill="none" stroke="#fff" stroke-width="0.8"/>
      </svg>
      <span class="rule" style="width:46px"></span>
    </div>

    <div class="block contact-lines">
      <p>(403)871-2964</p>
      <p>Shinebarnautocare@mailbox-example.com</p>
      <p>www.<span class="accent">Shinebarnautocare</span>.com</p>
    </div>

    <div class="divider" style="top:500px">
      <span class="rule" style="width:75px"></span>
      <svg class="contact-icon" viewBox="0 0 26 26" aria-label="Location">
        <circle cx="13" cy="13" r="11.5" fill="none" stroke="#990000" stroke-width="1.5"/>
        <path d="M13 20s-5-5.2-5-9a5 5 0 0 1 10 0c0 3.8-5 9-5 9z" fill="#990000"/>
        <circle cx="13" cy="11" r="1.8" fill="#fff"/>
      </svg>
      <span class="rule" style="width:82px"></span>
    </div>
    <p class="block city">Carrow Bend, Sk</p>
  </section>

</div>
</body>
</html>
```